website design + images

We need a very appealing website design, layout and images for a sales analytics and sales productivity services company based in San Ramon, California. We need a good design for the home page and a template for all other pages (total 2 designs), and images for all inner pages (center column/banner images, and right hand top corner small images). There are about 18 inner pages.
Updates

Our existing website is www.vorlaxen.com
Our corporate colours are the ones that are there on the website. The logo is also shown. We will be changing the tagline to "accelerating revenue" or equivalent of that.

Please use the document "website for vorlaxen - template v2.doc" that I just uploaded for any reference to the content, navigation and wireframes. A few more clarifications are provided mainly for the link "Solutions".

Devendra Kothuri

Hi,
We just uploaded ver 4 of the website template. There is more elaboration provided around the sublinks / sections for Solutions. Pls review and do get back if you need any clarifications.

Rgds
Devendra Kothuri

Hi all,
We have so far received a few good designs. The designs are more or less on the right track. I would like to urge all of you to use the content and navigation provided in the document attached to our brief "website for vorlaxen - template v4.doc".  Please DO NOT use the content in our existing website www.vorlaxen.com . That is very old. We mentioned it only for reference to colour theme and broad details.

We have totally 13 sections in Solutions pages. They may be designed as a tree of links - first level sublinks - second level sublinks or links - first level sublinks and the remaining as sections within the first level sublinks pages. The page design would remain the same for all inner pages except careers. But after finalizing the design for the inner page, we will need images for the different inner pages.

Rgds
Devendra Kothuri

Hi,
Thank you all for participation and very good designs. We are quite happy with what we have seen. We have now shortlisted about 4 vendors and sending invididual feedback to them for further improvement. We will be finalizing by Monday or Tuesday.  To the vendors who do not get feedback from us, thank you very much for participation. We may still do business in future for some of our other needs. 
The following are the process steps / expectations going forward, 
1. Feedback to the shortlisted designers and inviting improvements.
2. Review of the improved designs and further shortlist & feedback or direct finalization.
3. The design should be in 1024*768
2. Number of page designs = 2 (home page, inner page).
4. Home page design: instead of delivery model and customers, show one link "Why Us".
4. Solutions page design:  We will be needing an image in center column of solutions page that in a nutshell gives all the different types of solutions we provide. The entire set of solutions is in our attached document website for vorlaxen - template v4 and I am just uploading v5 with more description on sublinks.
5. After selection, we will be needing images for all the solution pages (total 12 pages under solutions + one solutions page), 1 image for Why Us?, 1 for Careers, and 3 for company (about us/ team, core values, ...) = total 18

Rgds
Devendra Kothuri

Target Market(s)

We are a sales analytics and sales productivity services company. We help B2B companies with: sales planning; sales operations and sales measurement. The characteristics of our customers are:
- B2B medium enterprises (USD 100M- USD 2B in revenue) in the US
- Primary target verticals are: high-tech, engineering and professional services firms
- Our primary target customers titles are VP of Sales or VP of marketing; we could be selling to the CEO at companies with revenues below $200M

Industry/Entity Type

Consulting

Requirements
Must have
• - Clean, uncluttered design
• - Easy navigation; minimum clicks
Nice to have
• We have already built a content management system and wireframes for this site. To the extent possible, it would be great to leverage the wireframe structure we built, provided you don’t have to compromise on the look and feel and navigation of the site. Below is what we currently have as banner sizes and resolutions are:
• Home page banner size: 950 * 250’
• All pages – center top - image size: 558 * 160
• All pages – right hand top image – 175*135’

```html
<!DOCTYPE html>
<html lang="en">
<head>
<meta charset="utf-8">
<title>Vorlaxen</title>
<link rel="stylesheet" href="https://fonts.googleapis.com/css2?family=Arimo:wght@400;700&family=Questrial&family=Noto+Sans:wght@400;700&display=swap">
<style>
  :root {
    --blue: #0d5ea8;
    --blue-light: #1e7fd0;
    --blue-dark: #06488c;
    --navy-frame: #1a2744;
    --green: #6ab04c;
    --green-dark: #3f8a2f;
    --gray-top: #ffffff;
    --gray-bottom: #dcdcdc;
    --white: #ffffff;
  }
  * { box-sizing: border-box; margin: 0; padding: 0; }
  html, body { width: 1200px; height: 992px; overflow: hidden; }
  body { position: relative; background: var(--white); font-family: "Arimo", Arial, sans-serif; color: var(--white); }

  .site-header { position: absolute; left: 0; top: 0; width: 1200px; height: 120px; background: var(--white); }
  .brand { position: absolute; left: 20px; top: 36px; font-family: "Arimo", Arial, sans-serif; font-size: 42px; font-weight: 700; line-height: 48px; color: var(--blue); }

  .utility-links { position: absolute; left: 797px; top: 12px; width: 317px; height: 35px; border: 1px solid var(--blue); display: flex; align-items: center; justify-content: center; font-size: 14px; color: var(--blue); }

  .main-nav { position: absolute; top: 71px; left: 0; }
  .main-nav a { position: absolute; top: 0; height: 37px; display: flex; align-items: center; justify-content: center; font-family: "Arimo", Arial, sans-serif; font-weight: 700; font-size: 15px; color: var(--white); text-decoration: none; background: linear-gradient(var(--blue-light), var(--blue-dark)); border: 1px solid #0a3f78; box-shadow: inset 0 1px 0 rgba(255,255,255,.35); }

  .hero { position: absolute; left: 0; top: 120px; width: 1200px; height: 350px; background: linear-gradient(var(--blue-light), var(--blue-dark)); }
  .hero-title { position: absolute; left: 35px; top: 30px; font-family: "Noto Sans", Arial, sans-serif; font-weight: 400; font-size: 38px; }
  .hero-copy { position: absolute; left: 35px; top: 88px; width: 605px; font-size: 16px; line-height: 20px; }
  .hero-more { position: absolute; left: 560px; top: 296px; font-weight: 700; font-size: 15px; }
  .hero-frame { position: absolute; left: 678px; top: 8px; width: 441px; height: 334px; background: var(--navy-frame); padding: 10px; }
  .hero-photo { width: 100%; height: 100%; background: linear-gradient(#ffffff, #e8ebf0 70%, #cfd4dc); }

  .services { position: absolute; left: 0; top: 470px; width: 1200px; height: 482px; background: linear-gradient(var(--gray-top), var(--gray-bottom)); }
  .service-card { position: absolute; top: 63px; width: 259px; height: 370px; background: var(--blue); border-radius: 0 0 10px 10px; }
  .service-card h2 { height: 50px; display: flex; align-items: center; justify-content: center; background: linear-gradient(var(--green), var(--green-dark)); border: 1px solid var(--green-dark); font-family: "Questrial", Arial, sans-serif; font-weight: 400; font-size: 18px; color: var(--white); }
  .service-photo { position: absolute; left: 19px; top: 73px; width: 221px; height: 147px; border: 1px solid #cfd8e0; }
  .service-text { position: absolute; left: 16px; top: 245px; width: 232px; font-family: "Noto Sans", Arial, sans-serif; font-size: 12.5px; line-height: 16px; }
  .service-more { position: absolute; right: 20px; top: 337px; font-family: "Noto Sans", Arial, sans-serif; font-weight: 700; font-size: 14px; }

  .slider-arrow { position: absolute; top: 198px; width: 56px; height: 56px; }

  .site-footer { position: absolute; left: 0; top: 952px; width: 1200px; height: 40px; background: var(--blue); display: flex; align-items: center; justify-content: center; font-family: "Noto Sans", Arial, sans-serif; font-size: 13px; }
</style>
</head>
<body>
  <header class="site-header">
    <div class="brand">Vorlaxen</div>
    <div class="utility-links">Sign in (register) | Contact us | Sitemap</div>
    <nav class="main-nav">
      <a href="#" style="left:656px;width:78px">Home</a>
      <a href="#" style="left:740px;width:94px">Solutions</a>
      <a href="#" style="left:840px;width:78px">Why Us</a>
      <a href="#" style="left:924px;width:96px">company</a>
      <a href="#" style="left:1026px;width:88px">Careers</a>
    </nav>
  </header>

  <section class="hero">
    <h1 class="hero-title">Welcome to Vorlaxen</h1>
    <p class="hero-copy">Lorem ipsum dolor sit amet, consectetur adipiscing elit. Sed sagittis interdum justo, ac hendrerit libero porta ac. Quisque semper, quam sed elementum iaculis, est lectus suscipit nulla, at tincidunt turpis orci ut sapien. Aliquam erat volutpat. Sed sit amet nulla lacus, sit amet fringilla quam. Aliquam erat volutpat. Aliquam eu eros lacus. Nam a erat fermentum enim accumsan mattis. Duis bibendum nisi quis est ultricies pretium. Nam quam erat, aliquam nec cursus accumsan, ornare sed purus. Aliquam nec est mauris. Vivamus arcu enim, egestas in condimentum at, venenatis ut odio. Proin quis ullamcorper felis. Suspendisse ac nunc in tellus interdum suscipit quis sed erat.</p>
    <span class="hero-more">Read More</span>
    <div class="hero-frame">
      <div class="hero-photo" role="img" aria-label="Photo of a business team in dark suits standing together"></div>
    </div>
  </section>

  <section class="services">
    <svg class="slider-arrow" style="left:10px" viewBox="0 0 56 56" aria-label="Previous"><circle cx="28" cy="28" r="27" fill="#0d5ea8"/><path d="M14 28 L42 16 L35 28 L42 40 Z" fill="#fff"/></svg>

    <article class="service-card" style="left:72px">
      <h2>Sales Managemet Analytics</h2>
      <div class="service-photo" role="img" aria-label="Illustration of a rising orange and red bar chart with an arrow" style="background:linear-gradient(135deg,#f4f4f4,#f0b040 55%,#d62a1a)"></div>
      <p class="service-text">Lorem ipsum dolor sit amet, elit interdum justo, ac hendrerit libero porta ac. dolor sit amet, dolor sit amet, Quisque semper.</p>
      <span class="service-more">Read More</span>
    </article>

    <article class="service-card" style="left:336px">
      <h2>Sales Planning Analytics</h2>
      <div class="service-photo" role="img" aria-label="Photo of colleagues planning around a laptop" style="background:linear-gradient(135deg,#d8d2c8,#6e665c 60%,#2c2a28)"></div>
      <p class="service-text">Lorem ipsum dolor sit amet, elit interdum justo, ac hendrerit libero porta ac. dolor sit amet, dolor sit amet, Quisque semper.</p>
      <span class="service-more">Read More</span>
    </article>

    <article class="service-card" style="left:600px">
      <h2>Sales Operation Support</h2>
      <div class="service-photo" role="img" aria-label="Photo of a support agent wearing a headset" style="background:linear-gradient(135deg,#8a4a22,#c98a5c 50%,#3a4a5a)"></div>
      <p class="service-text">Lorem ipsum dolor sit amet, elit interdum justo, ac hendrerit libero porta ac. dolor sit amet, dolor sit amet, Quisque semper.</p>
      <span class="service-more">Read More</span>
    </article>

    <article class="service-card" style="left:864px">
      <h2>Testimonials</h2>
      <div class="service-photo" role="img" aria-label="Photo of a hand signing a document with a pen" style="background:linear-gradient(135deg,#f2e4cc,#d8a878 55%,#f6efe4)"></div>
      <p class="service-text">Lorem ipsum dolor sit amet, elit interdum justo, ac hendrerit libero porta ac. dolor sit amet, dolor sit amet, Quisque semper.</p>
      <span class="service-more">Read More</span>
    </article>

    <svg class="slider-arrow" style="left:1136px" viewBox="0 0 56 56" aria-label="Next"><circle cx="28" cy="28" r="27" fill="#0d5ea8"/><path d="M42 28 L14 16 L21 28 L14 40 Z" fill="#fff"/></svg>
  </section>

  <footer class="site-footer">Copyright Vorlaxen 2010. All Rights Reserverd</footer>
</body>
</html>
```